Lantern

My company name is lantern. The logo is attached. I am the business owner.
Name Gordon Pileck
Phone number- 2018347265
email- Gordon_pileck@mailbrook.net
Website is not live yet but it will be workwithlantern.com
the current beta link is- https://site.qvbtstage.com/lantern-v3/
on the back write “ find creative pros”
Use that beta link as reference for typography and colors on card.

```html
<!DOCTYPE html>
<html lang="en">
<head>
<meta charset="UTF-8">
<title>Lantern – Business Card</title>
<link href="https://fonts.googleapis.com/css2?family=Montserrat:wght@400;500;800&family=Oswald:wght@600&display=swap" rel="stylesheet">
<style>
  :root {
    --stage: #2b2b2b;
    --card: #141414;
    --card-edge: #1d1d1d;
    --ink: #ececec;
    --ink-soft: #d4d4d4;
  }
  * { box-sizing: border-box; margin: 0; padding: 0; }
  html, body {
    width: 1200px; height: 881px; overflow: hidden;
    background: var(--stage);
  }
  .canvas {
    width: 1200px; height: 881px;
    display: flex; flex-direction: column; align-items: center; justify-content: center;
    gap: 56px;
  }
  .card {
    position: relative;
    width: 620px; height: 354px;
    border-radius: 22px;
    background: linear-gradient(135deg, var(--card-edge) 0%, var(--card) 55%, #101010 100%);
    color: var(--ink);
    overflow: hidden;
  }
  .wordmark {
    font-family: "Montserrat", sans-serif;
    font-weight: 800;
    color: var(--ink);
    letter-spacing: 1px;
    line-height: 1;
    white-space: nowrap;
  }
  /* back */
  .card--back .wordmark {
    position: absolute; left: 0; right: 0; top: 118px;
    text-align: center; font-size: 72px;
  }
  .tagline {
    position: absolute; left: 0; right: 0; top: 246px;
    text-align: center;
    font-family: "Montserrat", sans-serif; font-weight: 400;
    font-size: 15px; letter-spacing: 4px; color: var(--ink-soft);
  }
  /* front */
  .card--front .wordmark {
    position: absolute; left: 150px; top: 58px; font-size: 72px;
  }
  .person {
    position: absolute; right: 318px; top: 234px; text-align: right;
    white-space: nowrap;
  }
  .person__name {
    font-family: "Oswald", sans-serif; font-weight: 600;
    font-size: 34px; letter-spacing: 2px; line-height: 1;
  }
  .person__role {
    font-family: "Montserrat", sans-serif; font-weight: 400;
    font-size: 14px; color: var(--ink-soft); margin-top: 3px;
  }
  .divider {
    position: absolute; left: 318px; top: 198px;
    width: 1.5px; height: 88px; background: var(--ink-soft);
  }
  .contacts {
    position: absolute; left: 336px; top: 198px;
    list-style: none;
    font-family: "Montserrat", sans-serif; font-weight: 500;
    font-size: 14px; color: var(--ink);
    white-space: nowrap;
  }
  .contacts li { display: flex; align-items: center; gap: 7px; height: 29px; }
  .contacts svg { width: 13px; height: 13px; flex: none; }
</style>
</head>
<body>
<main class="canvas">
  <section class="card card--back">
    <div class="wordmark">LANTERN</div>
    <p class="tagline">FIND CREATIVE PROS</p>
  </section>

  <section class="card card--front">
    <div class="wordmark">LANTERN</div>
    <div class="person">
      <div class="person__name">GORDON PILECK</div>
      <div class="person__role">Director</div>
    </div>
    <div class="divider"></div>
    <ul class="contacts">
      <li>
        <svg viewBox="0 0 16 16" fill="none" stroke="currentColor" stroke-width="1.6"><path d="M4 1.5l2.5 3-1.5 2c1 2 2.5 3.5 4.5 4.5l2-1.5 3 2.5-1.5 2.5C7 15 1 9 1.5 3z"/></svg>
        <span>2018347265</span>
      </li>
      <li>
        <svg viewBox="0 0 16 16" fill="none" stroke="currentColor" stroke-width="1.5"><rect x="1.5" y="3.5" width="13" height="9"/><path d="M1.5 3.5l6.5 5 6.5-5"/></svg>
        <span>Gordon_pileck@mailbrook.net</span>
      </li>
      <li>
        <svg viewBox="0 0 16 16" fill="none" stroke="currentColor" stroke-width="1.3"><circle cx="8" cy="8" r="6.5"/><ellipse cx="8" cy="8" rx="3" ry="6.5"/><path d="M1.5 8h13M2.5 4.8h11M2.5 11.2h11"/></svg>
        <span>www.workwithlantern.com</span>
      </li>
    </ul>
  </section>
</main>
</body>
</html>
```